Chiropractic Business Card

I need a business card designed to help me stand apart from my competition. I really like simple, clean designs that appear open and inviting. I would like the designs to incorporate the color blue, green, or both. I really like the attached picture because it highlights that I just don't treat "back pain" and it being a nice computer graphic helps show that I have a modern practice. "Modern practice" meaning merging technology and most current research in my patient care.

My information is:

Wesley Marrin, DC
Phone- (707) 555-0182
Email- drwesleymarrin@example-mail.net
Website- www.pelhamchiropractic.example
Address- 248 Tolliver Street, Sonoma, CA 95476

Jpeg and pdf attached of Pelham Chiropractic logo.
Updates

Atmosphere to be clean lines and solid colors to be have gradient fading, but don't want too much going on with the fading. Simple.

Target Market(s)

Active adults who are health conscious between the ages of 20-70

Industry/Entity Type

Computer

Colors
0455a3
85cae6

Requirements
Must have
• Change color of Pelham chiropractic logo (maroon) to fit the rest of the design.
Nice to have
• Can separate the running image from the black background to have it work with the design.

```html
<!DOCTYPE html>
<html lang="en">
<head>
<meta charset="utf-8">
<title>Pelham Chiropractic – Business Card</title>
<link rel="stylesheet" href="https://fonts.googleapis.com/css2?family=Open+Sans:wght@400;600;700&display=swap">
<style>
  :root {
    --navy: #3d3f98;
    --cyan: #00aeef;
    --ink: #2b2b2b;
    --card: #ffffff;
    --backdrop: #e4e5e7;
    --font: "Open Sans", Arial, sans-serif;
  }
  * { box-sizing: border-box; margin: 0; padding: 0; }
  html, body { width: 1200px; height: 883px; overflow: hidden; }
  body { background: var(--backdrop); font-family: var(--font); position: relative; }

  .card {
    position: absolute;
    width: 620px;
    height: 340px;
    background: var(--card);
    border-radius: 34px;
    overflow: hidden;
    box-shadow: 0 6px 18px rgba(0,0,0,0.12);
  }
  .card--back  { left: 500px; top: 80px; }
  .card--front { left: 80px;  top: 463px; }

  /* back */
  .brand {
    position: absolute;
    left: 60px; top: 128px;
    font-weight: 700;
    font-size: 38px;
    line-height: 1.05;
    color: var(--navy);
    letter-spacing: 0.5px;
  }
  .back-band { position: absolute; top: 95px; height: 112px; right: 0; width: 285px; display: flex; }
  .back-band__web {
    flex: 0 0 232px; background: var(--navy); color: #fff;
    display: flex; align-items: center; justify-content: center;
    font-size: 8px; letter-spacing: 0.8px; text-transform: uppercase;
    white-space: nowrap;
  }
  .back-band__accent { flex: 1; background: var(--cyan); }

  /* front */
  .holder { position: absolute; left: 0; right: 0; top: 40px; text-align: center; color: var(--ink); }
  .holder__name { font-size: 25px; font-weight: 400; letter-spacing: 0.5px; text-transform: uppercase; }
  .holder__name b { font-weight: 700; }
  .holder__role { font-size: 12px; text-transform: uppercase; margin-top: 1px; }
  .holder__role b { font-weight: 700; }

  .front-band { position: absolute; left: 0; right: 0; top: 120px; height: 122px; }
  .front-band svg { position: absolute; inset: 0; }
  .contact {
    position: absolute; color: #fff; text-transform: uppercase;
    font-size: 15px; line-height: 1.25; text-align: center;
  }
  .contact--phone { left: 30px; width: 260px; top: 48px; }
  .contact--web { left: 315px; width: 305px; top: 16px; font-size: 13px; }

  .address {
    position: absolute; left: 0; right: 0; top: 262px;
    text-align: center; color: var(--ink); font-size: 13px; line-height: 1.3; text-transform: uppercase;
  }
  .address b { font-weight: 700; }
</style>
</head>
<body>

<section class="card card--back" aria-label="Business card back">
  <div class="brand">Pelham<br>Chiropractic</div>
  <div class="back-band">
    <div class="back-band__web">www.pelhamchiropractic.example</div>
    <div class="back-band__accent"></div>
  </div>
</section>

<section class="card card--front" aria-label="Business card front">
  <div class="holder">
    <div class="holder__name">Wesley <b>Marrin</b>, DC</div>
    <div class="holder__role"><b>Doctor</b> of Chiropractic</div>
  </div>

  <div class="front-band">
    <svg width="620" height="122" viewBox="0 0 620 122" aria-hidden="true">
      <rect x="0" y="0" width="330" height="122" fill="var(--cyan)"/>
      <rect x="0" y="0" width="18" height="122" fill="var(--navy)"/>
      <polygon points="292,0 620,0 620,122 322,122" fill="var(--navy)"/>
    </svg>
    <div class="contact contact--phone">Phone<br>(707) 555-0182</div>
    <div class="contact contact--web">Email &amp; Web<br>drwesleymarrin@example-mail.net<br>www.pelhamchiropractic.example</div>
  </div>

  <div class="address">248 <b>Tolliver Street</b><br><b>Sonoma, CA 95476</b></div>
</section>

</body>
</html>
```